Business Card For Nightclub Industry

We're looking for a business card for our company VelvetPulse. We're interested in finishing options including die-cut, foil, 2 opposing rounded corners (not 4 rounded corners) and spot UV.

The card should be elegant yet refined to reflect a high tech company.

The front of the cart should be bold with the velvetpulse logo across. IF you choose to use a foil option, apply it to the velvetpulse logo.

The back of the card will list our other company and product logos along with their related text and links.

Target Market(s)

video professionals
club owners
event promoters
nightclubs
DJs

Industry/Entity Type

Business

Contact Information for Business Card

Garth Ellison
Founder & CEO

VelvetPulse LLC <-- this line is optional as it is implied from the main logo
742 W. Calder Rd
Austin, TX 78719
888.412.3098 x517

Font styles to use
Sans Serif

Requirements
Must have
• Front side logo:
• VelvetPulse (logo attached)
• Premium Visuals For Live Events
• www.velvetpulse-example.com
• --------
• Back side of card logos (equal sizing):
• GlintForms (use velvetpulse logo as placeholder; we are working on that logo now)
• Custom 3D Logo Animations
• www.glintforms-example.com
• BrightArcs (use velvetpulse logo as placeholder; we are working on that logo now)
• Professional Laser Systems
• www.brightarcs-example.com
• Tempryx (logo)
• Visual Software & Media Servers
• www.tempryx-example.net
• ScreenHazeHQ (logo)
• Premixed DVDs & BluRay
• www.discglowhub-example.com
• Additional logos to add:
• CometFrame (logo)
• Cascading Fetchmate (logo)
• Quill Beams (logo)
• Clipzen (logo)
Nice to have
• Spot UV
• Foil
• Opposing Rounded Corners
• Matches the feel of our new website (attached pic)
• You are not required to implement the exact logo colors as they appear in the attachments. For instance, if you want to replace all the logos with chrome this might be a good option.

```html
<!DOCTYPE html>
<html lang="en">
<head>
<meta charset="utf-8">
<title>VelvetPulse Business Card</title>
<link rel="stylesheet" href="https://fonts.googleapis.com/css2?family=Open+Sans:wght@400&family=Arimo:wght@400&display=swap">
<style>
  :root {
    --backdrop-core: #262626;
    --backdrop-edge: #000000;
    --orange-light: #f9b233;
    --orange-mid: #f39224;
    --orange-deep: #e8601c;
    --orange-text: #e8541c;
    --card-white: #f7f7f7;
    --ink-dark: #333333;
    --icon-tile: #eeeeee;
    --icon-edge: #c9c9c9;
    --white: #ffffff;
  }
  html, body {
    margin: 0;
    padding: 0;
    width: 1200px;
    height: 979px;
    overflow: hidden;
  }
  body {
    background: radial-gradient(ellipse at 50% 60%, var(--backdrop-core) 0%, var(--backdrop-edge) 70%);
  }
  .card-stage {
    display: block;
    width: 1200px;
    height: 979px;
  }
  .name-text { font-family: "Open Sans", sans-serif; fill: var(--white); }
  .role-text { font-family: "Open Sans", sans-serif; fill: var(--white); }
  .brand-name { font-family: "Arimo", sans-serif; fill: var(--ink-dark); }
  .contact-text { font-family: "Arimo", sans-serif; fill: var(--orange-text); font-size: 12.3px; }
  .icon-tile { fill: var(--icon-tile); stroke: var(--icon-edge); stroke-width: 0.6; }
  .icon-glyph { fill: var(--orange-text); }
  .icon-line { fill: none; stroke: var(--orange-text); stroke-width: 1.2; }
</style>
</head>
<body>
<svg class="card-stage" viewBox="0 0 775 632" xmlns="http://www.w3.org/2000/svg">
  <defs>
    <radialGradient id="orangeGlow" cx="0.55" cy="0.55" r="0.7">
      <stop offset="0" stop-color="var(--orange-light)"/>
      <stop offset="0.6" stop-color="var(--orange-mid)"/>
      <stop offset="1" stop-color="var(--orange-deep)"/>
    </radialGradient>
    <linearGradient id="foldShade" x1="0" x2="1">
      <stop offset="0" stop-color="#d9621a"/>
      <stop offset="0.5" stop-color="#f7a42c"/>
      <stop offset="1" stop-color="#e27a1f"/>
    </linearGradient>
    <linearGradient id="chevronShade" x1="0" x2="1" y1="0" y2="0">
      <stop offset="0" stop-color="var(--orange-light)"/>
      <stop offset="1" stop-color="var(--orange-deep)"/>
    </linearGradient>
    <filter id="softShadow" x="-20%" y="-20%" width="140%" height="140%">
      <feDropShadow dx="0" dy="1" stdDeviation="1" flood-opacity="0.35"/>
    </filter>
    <clipPath id="cardShape">
      <path d="M137 176 H606 A80 80 0 0 1 686 256 V456 H237 A100 100 0 0 1 137 356 Z"/>
    </clipPath>
  </defs>

  <g class="business-card" clip-path="url(#cardShape)">
    <rect class="card-base" x="137" y="176" width="549" height="280" fill="url(#orangeGlow)"/>
    <rect class="fold-band" x="210" y="176" width="32" height="280" fill="url(#foldShade)" opacity="0.9"/>
    <path class="chevron-panel" d="M370 176 H427 V456 H370 L305 392 V240 Z" fill="url(#chevronShade)" filter="url(#softShadow)"/>
    <path class="info-panel" d="M427 176 H686 V456 H427 V436 L373 382 V268 L427 215 Z" fill="var(--card-white)" filter="url(#softShadow)"/>
  </g>

  <rect class="service-illustration" x="314" y="296" width="48" height="58" rx="3" fill="var(--orange-light)" opacity="0.85" role="img" aria-label="Line icon of a laptop with a stylus"/>

  <text class="name-text" font-size="21" transform="translate(235 400) rotate(-90)">Garth Ellison</text>
  <text class="role-text" font-size="14" transform="translate(262 390) rotate(-90)">Founder &amp; CEO</text>
  <text class="role-text" font-size="14" transform="translate(280 400) rotate(-90)">VelvetPulse LLC</text>

  <g class="brand-mark">
    <circle cx="448" cy="206" r="8" fill="var(--orange-text)"/>
    <text class="brand-name" x="463" y="214" font-size="23">velvetpulse</text>
  </g>

  <g class="contact-list">
    <g class="contact-item">
      <rect class="icon-tile" x="446" y="251" width="18" height="17" rx="2"/>
      <path class="icon-glyph" d="M451 255 l3 0 l1 3 l-1.5 1 a6 6 0 0 0 3 3 l1 -1.5 l3 1 l0 3 a9 9 0 0 1 -9.5 -9.5 z"/>
      <text class="contact-text" x="480" y="264">888.412.3098 x517</text>
    </g>
    <g class="contact-item">
      <rect class="icon-tile" x="446" y="275" width="18" height="17" rx="2"/>
      <rect class="icon-line" x="450" y="279" width="10" height="8"/>
      <path class="icon-line" d="M450 279 l5 4.5 l5 -4.5"/>
      <text class="contact-text" x="480" y="288">velvetpulse@example.com</text>
    </g>
    <g class="contact-item">
      <rect class="icon-tile" x="446" y="299" width="18" height="17" rx="2"/>
      <path class="icon-glyph" d="M455 302 l6 5.5 h-2 v5 h-8 v-5 h-2 z"/>
      <text class="contact-text" x="480" y="312">742 W. Calder Rd Austin, TX 78719</text>
    </g>
    <g class="contact-item">
      <rect class="icon-tile" x="446" y="323" width="18" height="17" rx="2"/>
      <text class="contact-text" x="480" y="337">profiles.example.com/velvetpulse</text>
    </g>
    <g class="contact-item">
      <rect class="icon-tile" x="446" y="347" width="18" height="17" rx="2"/>
      <text class="contact-text" x="480" y="360">social.example.com/velvetpulse</text>
    </g>
    <g class="contact-item">
      <rect class="icon-tile" x="446" y="371" width="18" height="17" rx="2"/>
      <text class="contact-text" x="480" y="384">@VelvetPulse</text>
    </g>
    <g class="contact-item">
      <rect class="icon-tile" x="446" y="395" width="18" height="17" rx="2"/>
      <circle class="icon-line" cx="455" cy="403.5" r="5"/>
      <path class="icon-line" d="M450 403.5 h10 M455 398.5 v10"/>
      <text class="contact-text" x="480" y="407">www.velvetpulse-example.com</text>
    </g>
  </g>
</svg>
</body>
</html>
```